Oakhaven Construction Need an information and interactive website with client portal. We have ou

Need to have a client log in screen for work orders and estimate requests.
Nice informational landing page.

Oakhaven is a full service general contractor servicing apartment complexes;
maintenance of grounds and apartments - remodeling and construction.

Design Specifics: We are pretty open here. Some good examples are
www.marrowpeakbuilders.com , tovelresidence.com and www.quillbyworksite.com

For the site we need:
Homepage - to explain services
Roofing page
Apartment Page
Client Portal - where clients can set up accounts to set up work/estimate request that will be routed to our email

--Will need coding, plan to host site on Wordpress

Target Market(s)

Multi family, Residential and commercial clients

Industry/Entity Type

Construction

Coding

Coded - Design and coding required

Number of Pages Required

3 page

Font styles to use
Serif

Requirements
Must have
• Client portal
Nice to have
• Not sure. please advise

```html
<!DOCTYPE html>
<html lang="en">
<head>
<meta charset="utf-8">
<title>Oakhaven Construction</title>
<link href="https://fonts.googleapis.com/css2?family=Open+Sans:wght@400;600;700;800&display=swap" rel="stylesheet">
<style>
:root{
  --red:#d3151e;
  --ink:#2b2b2b;
  --muted:#7a7a7a;
  --light:#f1f1f3;
  --dark:#2f2f30;
  --footer:#eeeeef;
  --bar:#3a3a3b;
  --white:#ffffff;
}
*{margin:0;padding:0;box-sizing:border-box}
html,body{width:1200px;height:3056px;overflow:hidden}
body{font-family:"Open Sans",Arial,sans-serif;color:var(--ink);background:var(--white);position:relative}
.section-title{font-size:25px;font-weight:700;text-align:center;text-transform:uppercase;letter-spacing:.3px}
.section-lead{font-size:13.5px;color:var(--muted);text-align:center;line-height:19px;width:640px;margin:14px auto 0}

/* header */
.site-header{height:94px;border-bottom:1px solid #ddd;display:flex;align-items:center;justify-content:space-between;padding:0 100px 0 88px}
.brand{display:flex;align-items:center;gap:10px;font-size:24px;font-weight:800;color:var(--red);letter-spacing:.5px}
.brand-mark{width:20px;height:20px;background:var(--red)}
.main-nav{display:flex;align-items:center;gap:8px}
.main-nav a{font-size:14px;font-weight:600;color:var(--ink);text-decoration:none;padding:8px 15px;border-radius:20px;text-transform:uppercase;display:flex;align-items:center;gap:6px}
.main-nav a.active{border:2px solid var(--red)}
.caret{width:9px;height:6px}

/* hero */
.hero{height:560px;position:relative;background:linear-gradient(180deg,#8d97a3 0%,#5e6670 45%,#3c4046 100%);text-align:center;color:var(--white)}
.hero-photo{position:absolute;inset:0;background:linear-gradient(90deg,rgba(40,42,46,.35),rgba(90,96,104,.1) 50%,rgba(40,42,46,.35))}
.hero-content{position:relative;padding-top:196px}
.hero h1{font-size:43px;font-weight:700;letter-spacing:.5px;text-shadow:0 2px 6px rgba(0,0,0,.4)}
.hero p{font-size:14px;line-height:20px;width:620px;margin:10px auto 0}
.btn-outline{display:inline-block;margin-top:22px;border:2px solid var(--white);border-radius:22px;padding:8px 18px;font-size:13px;font-weight:700;color:var(--white);text-decoration:none}
.scroll-cue{position:absolute;left:0;right:0;top:494px;font-size:9px;font-weight:600;letter-spacing:.5px}
.scroll-cue svg{display:block;margin:8px auto 0}

/* services */
.services{height:527px;padding-top:74px}
.service-grid{display:flex;justify-content:center;gap:12px;margin-top:52px}
.service{width:252px;text-align:center}
.service-photo{width:132px;height:132px;border-radius:50%;margin:0 auto;border:3px solid #e5e5e5}
.service h3{font-size:14px;font-weight:700;margin-top:20px}
.service p{font-size:12px;color:var(--muted);line-height:17px;margin-top:6px;padding:0 12px}
.read-more{display:inline-block;font-size:11px;font-weight:700;color:var(--ink);margin-top:8px;text-decoration:none}

/* about */
.about{height:318px;position:relative;background:var(--dark);color:var(--white);text-align:center}
.about-photo{position:absolute;inset:0;background:linear-gradient(90deg,#262626,#3a3a3a 50%,#2a2a2a)}
.about-content{position:relative;padding-top:78px}
.about .section-title{color:var(--white)}
.about p{font-size:13px;line-height:21px;width:740px;margin:18px auto 0}
.about .read-more{color:var(--white);font-size:13px;margin-top:12px}

/* projects */
.projects{height:493px;background:var(--light);padding-top:60px}
.project-grid{display:flex;justify-content:center;gap:30px;margin-top:38px}
.project{width:234px;height:183px;border:3px solid var(--white);box-shadow:0 1px 4px rgba(0,0,0,.15)}
.view-more{display:block;text-align:center;margin-top:40px;font-size:16px;font-weight:700;color:var(--red);text-decoration:none}

/* vision */
.vision{height:628px;padding-top:60px;position:relative}
.vision .section-title{font-size:21px}
.vision-person{position:absolute;left:478px;top:178px;width:132px;height:374px;background:linear-gradient(180deg,#e8893a 0%,#efeae4 25%,#e47a2a 55%,#4a4a4a 100%);border-radius:60px 60px 6px 6px}
.feature{position:absolute;width:190px;font-size:11.5px}
.feature h4{font-size:12px;font-weight:700;text-transform:uppercase;margin-bottom:6px}
.feature p{color:var(--muted);line-height:16px}
.feature.left{left:98px;text-align:right}
.feature.right{left:921px;text-align:left}
.hex{position:absolute;width:66px;height:74px}
.chain{position:absolute;width:2px;border-left:2px dotted var(--red)}

/* stats */
.stats{height:146px;background:var(--bar);display:flex;color:var(--white)}
.stat{flex:1;display:flex;flex-direction:column;align-items:center;padding-top:28px}
.stat strong{font-size:30px;font-weight:700;line-height:36px;margin-top:6px}
.stat span{font-size:11px;font-weight:700}

/* footer */
.site-footer{height:240px;background:var(--footer);position:relative}
.footer-col{position:absolute;top:38px}
.footer-col h5{font-size:19px;font-weight:400;text-transform:uppercase;margin-bottom:20px}
.contact-list li{list-style:none;display:flex;gap:14px;font-size:13px;line-height:17px;margin-bottom:14px;color:#444}
.contact-list svg{flex:none;margin-top:2px}
.link-list li{list-style:none;font-size:12.5px;line-height:21px;color:#444;display:flex;align-items:center;gap:10px}
.link-list.spaced li{line-height:30px}
.chev{color:var(--red);font-weight:700;font-size:12px}
.newsletter-input{width:268px;height:38px;border:1px solid #ccc;border-radius:20px;background:#e4e4e6;font-size:12px;color:#888;padding:0 18px;display:flex;align-items:center}
.btn-subscribe{display:inline-block;margin-top:18px;background:var(--red);color:var(--white);font-size:12px;font-weight:700;border-radius:18px;padding:9px 18px}
.copyright{height:50px;background:var(--bar);color:#ddd;font-size:12px;text-align:center;line-height:50px}
</style>
</head>
<body>

<header class="site-header">
  <div class="brand"><span class="brand-mark"></span>OAKHAVEN</div>
  <nav class="main-nav">
    <a class="active">Home</a>
    <a>About us</a>
    <a>Roofing <svg class="caret" viewBox="0 0 9 6"><path d="M1 1l3.5 3.5L8 1" fill="none" stroke="#2b2b2b" stroke-width="1.5"/></svg></a>
    <a>Apartment</a>
    <a>Client portal <svg class="caret" viewBox="0 0 9 6"><path d="M1 1l3.5 3.5L8 1" fill="none" stroke="#2b2b2b" stroke-width="1.5"/></svg></a>
    <a>Contact us</a>
  </nav>
</header>

<section class="hero">
  <div class="hero-photo" role="img" aria-label="Photo of modern white apartment buildings with balconies"></div>
  <div class="hero-content">
    <h1>OAKHAVEN CONSTRUCTION</h1>
    <p>Lorem Ipsum passages, and more recently with desktop publishing software like Quillset Layout including versions of Lorem Ipsum.</p>
    <a class="btn-outline">VIEW MORE</a>
  </div>
  <div class="scroll-cue">SCROLL HERE
    <svg width="16" height="28" viewBox="0 0 16 28"><rect x="1" y="1" width="14" height="26" rx="7" fill="none" stroke="#fff" stroke-width="1.5"/><line x1="8" y1="6" x2="8" y2="11" stroke="#fff" stroke-width="1.5"/></svg>
  </div>
</section>

<section class="services">
  <h2 class="section-title">Our Services</h2>
  <p class="section-lead">Curabitur quam etsum lacus etsumis nulatis etsumised vitae etimuned nisle varius loremis feugiat ligula aliquam ets vitae dictimus etis netsum.</p>
  <div class="service-grid">
    <div class="service">
      <div class="service-photo" role="img" aria-label="Photo of an apartment complex facade" style="background:radial-gradient(circle,#d9743a,#6b8fc0)"></div>
      <h3>APARTMENT COMPLEXES</h3>
      <p>Curabitur quam etsum lacus etsumis nulat iaculis ets vitae etsvariumis feuglats ligula netsum loremis.</p>
      <a class="read-more">READ MORE &gt;&gt;</a>
    </div>
    <div class="service">
      <div class="service-photo" role="img" aria-label="Photo of a worker maintaining an interior" style="background:radial-gradient(circle,#3f8f7a,#e8e6d8)"></div>
      <h3>MAINTENANCE OF GROUNDS</h3>
      <p>Curabitur quam etsum lacus etsumis nulat iaculis ets vitae etsvariumis feuglats ligula netsum loremis.</p>
      <a class="read-more">READ MORE &gt;&gt;</a>
    </div>
    <div class="service">
      <div class="service-photo" role="img" aria-label="Photo of a remodeled apartment living room" style="background:radial-gradient(circle,#8a6a52,#d9d2ca)"></div>
      <h3>APARTMENTS REMODELING</h3>
      <p>Curabitur quam etsum lacus etsumis nulat iaculis ets vitae etsvariumis feuglats ligula netsum loremis.</p>
      <a class="read-more">READ MORE &gt;&gt;</a>
    </div>
    <div class="service">
      <div class="service-photo" role="img" aria-label="Photo of a construction site under a blue sky" style="background:linear-gradient(180deg,#a9c3e0,#c9b08a)"></div>
      <h3>CONSTRUCTION</h3>
      <p>Curabitur quam etsum lacus etsumis nulat iaculis ets vitae etsvariumis feuglats ligula netsum loremis.</p>
      <a class="read-more">READ MORE &gt;&gt;</a>
    </div>
  </div>
</section>

<section class="about">
  <div class="about-photo" role="img" aria-label="Dark photo of construction workers on site"></div>
  <div class="about-content">
    <h2 class="section-title">About Us</h2>
    <p>Many desktop publishing packages and web page editors now use Lorem Ipsum as their default model text, and a search for 'lorem ipsum' will uncover many web sites still in their infancy.Various versions have evolved over the years, sometimes by accident, sometimes on Various versions have evolved over the years, sometimes by accident, sometimes on purpose but the majority have suffered alteration in some form, by injected humour.</p>
    <a class="read-more">READ MORE &gt;&gt;</a>
  </div>
</section>

<section class="projects">
  <h2 class="section-title">Latest Projects</h2>
  <p class="section-lead">Curabitur quam etsum lacus etsumis nulatis etsumised vitae etimuned nisle varius loremis feugiat ligula aliquam ets vitae dictimus etis netsum.</p>
  <div class="project-grid">
    <div class="project" role="img" aria-label="Photo of a high-rise under construction with a crane" style="background:linear-gradient(180deg,#3d7fcf,#b9a48a)"></div>
    <div class="project" role="img" aria-label="Photo of a finished apartment block" style="background:linear-gradient(180deg,#8fb6e2 0%,#dfe7ef 40%,#b07a55 75%,#7a8a3a)"></div>
    <div class="project" role="img" aria-label="Photo of a mason building a stone wall" style="background:linear-gradient(160deg,#5f8a3a,#8a8175 60%,#c3a57a)"></div>
    <div class="project" role="img" aria-label="Photo of a renovated laundry room" style="background:linear-gradient(90deg,#e4e3e0,#b9b7b2 60%,#eeeeec)"></div>
  </div>
  <a class="view-more">VIEW MORE &gt;&gt;</a>
</section>

<section class="vision">
  <h2 class="section-title">Our Vision</h2>
  <p class="section-lead">Curabitur quam etsum lacus etsumis nulatis etsumised vitae etimuned nisle varius loremis feugiat ligula aliquam ets vitae dictimus etis netsum.</p>

  <div class="vision-person" role="img" aria-label="Photo of a construction engineer in a hard hat holding plans"></div>

  <span class="chain" style="left:341px;top:301px;height:156px"></span>
  <span class="chain" style="left:861px;top:301px;height:156px"></span>

  <div class="feature left" style="top:234px"><h4>Passion for construction</h4><p>Nemo enim ipsam voluptatem quia voluptas aspernatur netsum loremis fugitsum sed ratione.</p></div>
  <div class="feature left" style="top:348px"><h4>Lorem ipsum is not simply</h4><p>Nemo enim ipsam voluptatem quia voluptas aspernatur netsum loremis fugitsum sed ratione.</p></div>
  <div class="feature left" style="top:462px"><h4>Suffered alteration</h4><p>Nemo enim ipsam voluptatem quia voluptas aspernatur netsum loremis fugitsum sed ratione.</p></div>

  <div class="feature right" style="top:234px"><h4>Lorem ipsum available</h4><p>Nemo enim ipsam voluptatem quia voluptas aspernatur netsum loremis fugitsum sed ratione.</p></div>
  <div class="feature right" style="top:348px"><h4>Finibus bonorum lorum</h4><p>Nemo enim ipsam voluptatem quia voluptas aspernatur netsum loremis fugitsum sed ratione.</p></div>
  <div class="feature right" style="top:462px"><h4>Generated lorem ipsum</h4><p>Nemo enim ipsam voluptatem quia voluptas aspernatur netsum loremis fugitsum sed ratione.</p></div>

  <svg class="hex" style="left:309px;top:227px" viewBox="0 0 66 74"><polygon points="33,2 64,19 64,55 33,72 2,55 2,19" fill="#fff" stroke="#d3151e" stroke-width="1.5"/><g fill="#d3151e"><path d="M21 31h24l-12-7z"/><rect x="23" y="33" width="3" height="10"/><rect x="31.5" y="33" width="3" height="10"/><rect x="40" y="33" width="3" height="10"/><rect x="21" y="44" width="24" height="3"/></g></svg>
  <svg class="hex" style="left:309px;top:341px" viewBox="0 0 66 74"><polygon points="33,2 64,19 64,55 33,72 2,55 2,19" fill="#fff" stroke="#d3151e" stroke-width="1.5"/><g fill="#d3151e"><path d="M19 33l14-7 14 7-14 7z"/><path d="M25 37v6c0 2 4 4 8 4s8-2 8-4v-6l-8 4z"/></g></svg>
  <svg class="hex" style="left:309px;top:457px" viewBox="0 0 66 74"><polygon points="33,2 64,19 64,55 33,72 2,55 2,19" fill="#fff" stroke="#d3151e" stroke-width="1.5"/><circle cx="33" cy="37" r="11" fill="#d3151e"/><circle cx="33" cy="37" r="4" fill="#fff"/></svg>

  <svg class="hex" style="left:829px;top:227px" viewBox="0 0 66 74"><polygon points="33,2 64,19 64,55 33,72 2,55 2,19" fill="#fff" stroke="#d3151e" stroke-width="1.5"/><rect x="23" y="27" width="20" height="20" rx="3" fill="#d3151e"/></svg>
  <svg class="hex" style="left:829px;top:341px" viewBox="0 0 66 74"><polygon points="33,2 64,19 64,55 33,72 2,55 2,19" fill="#fff" stroke="#d3151e" stroke-width="1.5"/><g fill="none" stroke="#d3151e" stroke-width="2"><path d="M33 25l11 6v12l-11 6-11-6V31z"/><path d="M22 31l11 6 11-6M33 37v12"/></g></svg>
  <svg class="hex" style="left:829px;top:457px" viewBox="0 0 66 74"><polygon points="33,2 64,19 64,55 33,72 2,55 2,19" fill="#fff" stroke="#d3151e" stroke-width="1.5"/><g fill="#d3151e"><ellipse cx="33" cy="28" rx="10" ry="3.5"/><rect x="23" y="31" width="20" height="5" rx="2"/><rect x="23" y="38" width="20" height="5" rx="2"/><rect x="23" y="45" width="20" height="4" rx="2"/></g></svg>
</section>

<section class="stats">
  <div class="stat">
    <svg width="30" height="26" viewBox="0 0 30 26"><path d="M15 25S1 16 1 8a7 7 0 0 1 14-2 7 7 0 0 1 14 2c0 8-14 17-14 17z" fill="#fff"/></svg>
    <strong>1,250</strong><span>Happy Clients</span>
  </div>
  <div class="stat">
    <svg width="32" height="28" viewBox="0 0 32 28"><g fill="#fff"><path d="M2 9h28L16 1z"/><rect x="5" y="11" width="4" height="11"/><rect x="14" y="11" width="4" height="11"/><rect x="23" y="11" width="4" height="11"/><rect x="2" y="24" width="28" height="4"/></g></svg>
    <strong>2,780</strong><span>Finished Projects</span>
  </div>
  <div class="stat">
    <svg width="26" height="28" viewBox="0 0 26 28"><g fill="#fff"><circle cx="13" cy="7" r="6.5"/><path d="M1 28c0-8 5-13 12-13s12 5 12 13z"/></g></svg>
    <strong>174</strong><span>Qualified Workers</span>
  </div>
  <div class="stat">
    <svg width="32" height="28" viewBox="0 0 32 28"><g fill="#fff"><path d="M16 1L1 14h4v13h8v-8h6v8h8V14h4z"/></g></svg>
    <strong>1,120</strong><span>Refurbished Houses</span>
  </div>
</section>

<footer class="site-footer">
  <div class="footer-col" style="left:86px">
    <h5>Contact us</h5>
    <ul class="contact-list">
      <li><svg width="12" height="16" viewBox="0 0 12 16"><path d="M6 0a6 6 0 0 0-6 6c0 4.5 6 10 6 10s6-5.5 6-10a6 6 0 0 0-6-6zm0 8.5A2.5 2.5 0 1 1 6 3.5a2.5 2.5 0 0 1 0 5z" fill="#d3151e"/></svg><span>18 Cedar Row, Suite 200<br>Millbrook</span></li>
      <li><svg width="14" height="14" viewBox="0 0 14 14"><path d="M3 0l3 3-1.5 2a8 8 0 0 0 4.5 4.5L11 8l3 3-2 3C6 14 0 8 0 2z" fill="#d3151e"/></svg><span>555-201-4836</span></li>
      <li><svg width="16" height="12" viewBox="0 0 16 12"><rect width="16" height="12" rx="1.5" fill="#d3151e"/><path d="M1 1.5l7 5 7-5" fill="none" stroke="#eeeeef" stroke-width="1.3"/></svg><span>info@oakhavenbuild.com</span></li>
    </ul>
  </div>
  <div class="footer-col" style="left:361px">
    <h5>Quick links</h5>
    <ul class="link-list">
      <li><span class="chev">›</span>Home</li>
      <li><span class="chev">›</span>About us</li>
      <li><span class="chev">›</span>Roofing</li>
      <li><span class="chev">›</span>Apartment</li>
      <li><span class="chev">›</span>Client Portal</li>
      <li><span class="chev">›</span>Contact us</li>
    </ul>
  </div>
  <div class="footer-col" style="left:577px">
    <h5>Services</h5>
    <ul class="link-list spaced">
      <li><span class="chev">›</span>Apartment complexes</li>
      <li><span class="chev">›</span>Maintenance of grounds</li>
      <li><span class="chev">›</span>Apartments - remodeling</li>
      <li><span class="chev">›</span>Construction.</li>
    </ul>
  </div>
  <div class="footer-col" style="left:843px">
    <h5>Newsletter</h5>
    <div class="newsletter-input">E-mail address...</div>
    <span class="btn-subscribe">SUBSCRIBE</span>
  </div>
</footer>

<div class="copyright">@copyright 2016 Oakhaven Construction.All Rights Reserved</div>

</body>
</html>
```